Its just a copy of my concept with little changes.
Be careful you have to come with your unique concept.
All - I'm not sure how some of you are using a prior generation of my logo design, but in the final design (which I did upload for this project), the words in the tagline are flipped so Insight appears first. Please be sure you are using proper version. Thanks! Dot
All - I think the fax number should immediately follow the phone as the numbers are consecutive. Please do not include the cell phone on the letterhead, just on the business card. Appeals, Commercial Litigation (my practice areas) needs to be specified on both. Thanks!
Please note this is a combined project with Hallbrook Law Branding. I'm working with tech support to change the project names so it's clear this is a package. Thanks!
Thanks for all your great work and creativity! This is going to be a hard decison.
Dot

```html
<!DOCTYPE html>
<html lang="en">
<head>
<meta charset="utf-8">
<title>Hallbrook Law – Business Card</title>
<link rel="stylesheet" href="https://fonts.googleapis.com/css2?family=Cormorant+Garamond:wght@500;600&display=swap">
<style>
  :root {
    --page: #ffffff;
    --frame: #4a4a4a;
    --ink: #3b3835;
    --gold: #a9793a;
    --gold-light: #e3c58f;
    --gold-fade: rgba(169, 121, 58, 0);
  }
  html, body {
    margin: 0;
    padding: 0;
    width: 1200px;
    height: 751px;
    overflow: hidden;
    background: var(--page);
  }
  .card {
    position: absolute;
    left: 72px;
    top: 72px;
    width: 1075px;
    height: 612px;
    box-sizing: border-box;
    border: 2px solid var(--frame);
    background: var(--page);
    font-family: "Cormorant Garamond", Georgia, serif;
    color: var(--ink);
  }
  .brand {
    position: absolute;
    left: 46px;
    top: 84px;
    display: flex;
    align-items: center;
    gap: 16px;
    color: var(--gold);
    font-weight: 600;
    font-variant: small-caps;
  }
  .brand-mark {
    width: 48px;
    height: 48px;
    background: var(--gold);
  }
  .brand-name {
    line-height: 1;
  }
  .brand-name .prefix {
    display: block;
    font-size: 26px;
    letter-spacing: 1px;
    padding-left: 60px;
  }
  .brand-name .name {
    display: block;
    font-size: 42px;
    letter-spacing: 0.5px;
  }
  .rule {
    position: absolute;
    height: 9px;
  }
  .rule-top {
    left: 540px;
    top: 137px;
    width: 520px;
    background: linear-gradient(90deg, var(--gold-fade) 0%, var(--gold) 55%, var(--gold-light) 80%, var(--gold) 100%);
  }
  .rule-bottom {
    left: 3px;
    top: 533px;
    width: 510px;
    background: linear-gradient(90deg, var(--gold) 0%, var(--gold-light) 20%, var(--gold) 45%, var(--gold-fade) 100%);
  }
  .person {
    position: absolute;
    left: 88px;
    top: 280px;
    font-weight: 500;
    font-variant: small-caps;
  }
  .person-name {
    margin: 0;
    font-size: 44px;
    font-weight: 500;
    letter-spacing: 1px;
    line-height: 1;
  }
  .practice {
    margin: 6px 0 0;
    font-size: 27px;
    letter-spacing: 1px;
  }
  .contact {
    position: absolute;
    right: 66px;
    top: 470px;
    margin: 0;
    text-align: right;
    font-style: normal;
    font-size: 23px;
    font-weight: 500;
    font-variant: small-caps;
    letter-spacing: 0.8px;
    line-height: 30px;
  }
  .contact span {
    display: block;
  }
</style>
</head>
<body>
  <div class="card">
    <div class="brand">
      <div class="brand-mark" aria-hidden="true"></div>
      <div class="brand-name">
        <span class="prefix">Law Office of</span>
        <span class="name">Dorothy B. Hallbrook</span>
      </div>
    </div>

    <div class="rule rule-top"></div>

    <div class="person">
      <h1 class="person-name">Dot Hallbrook</h1>
      <p class="practice">Appeals | Commercial Litigation</p>
    </div>

    <address class="contact">
      <span>1850 W. Cedar Ridge Road, Marlowe, Arizona 85099-1420</span>
      <span>Phone: 555-014-2252 | Fax: 555-014-2253 | Cell: 555-019-6016</span>
      <span>Email: dothallbrook@mailbox.net | www.HallbrookLawAZ.com</span>
    </address>

    <div class="rule rule-bottom"></div>
  </div>
</body>
</html>
```